SPICE LABEL DESIGN FOR A TASTY DRY RUB! (chicken, ribs, wings)

Looking for a fun/creative/edgy label for a spice jar! The label will be rectangular (exact size tbd - but approximately 1.2" W X 3" H).
This spice is a dry rub blend of 14 EPIC spices, to be used on chicken, chicken wings, ribs, etc.
Copywritting on the label to be;
Tova JK's Blaze BBQ Rub
A blend of 14 UNTOVAGETTABLE spices
*Note the word "untovagettabe" is spelt incorectly on purpose for a play a words with "tova". Please use a different color font for "tova" within the word.
Also would like "Tova JK's" to be prominent
Looking for an illustration/design that is fun/creative/catchy/edgy/appealing! While still keeping the design appealing to higher end markets. Have fun with it and think outside of the box!! :)
People who enjoy cooking, young adults and adults, display at restaurants or retail markets

```html
<!DOCTYPE html>
<html lang="en">
<head>
<meta charset="utf-8">
<title>Tova JK's Blaze BBQ Rub – Spice Label</title>
<link rel="stylesheet" href="https://fonts.googleapis.com/css2?family=Alfa+Slab+One&family=Ultra&family=Oswald:wght@500&family=Montserrat:wght@500&display=swap">
<style>
  :root {
    --backdrop: #f9d1aa;
    --label-black: #0b0908;
    --charcoal: #1c1715;
    --ember: #7a2a0c;
    --flame: #e0661f;
    --flame-hot: #f5a23a;
    --tan: #c9a36b;
    --brand-red: #d1343f;
    --steel: #6d6e71;
    --white: #ffffff;
  }
  html, body {
    margin: 0;
    padding: 0;
    width: 1200px;
    height: 3206px;
    overflow: hidden;
    background: var(--backdrop);
  }
  .canvas {
    position: relative;
    width: 1200px;
    height: 3206px;
    background: var(--backdrop);
  }
  .label {
    position: absolute;
    left: 376px;
    top: 183px;
    width: 448px;
    height: 1120px;
    background: var(--white);
    box-shadow: 10px 12px 16px rgba(90, 50, 20, 0.28);
    overflow: hidden;
  }
  .label__artwork {
    position: absolute;
    left: 0;
    top: 0;
    width: 448px;
    height: 971px;
    background:
      radial-gradient(ellipse 22% 12% at 4% 96%, var(--flame-hot) 0%, rgba(224,102,31,0) 100%),
      radial-gradient(ellipse 40% 22% at 8% 90%, var(--flame) 0%, rgba(224,102,31,0.35) 40%, rgba(11,9,8,0) 100%),
      radial-gradient(ellipse 55% 35% at 0% 78%, rgba(196,82,26,0.55) 0%, rgba(122,42,12,0.3) 45%, rgba(11,9,8,0) 100%),
      radial-gradient(ellipse 30% 20% at 100% 70%, rgba(196,82,26,0.25) 0%, rgba(11,9,8,0) 100%),
      radial-gradient(ellipse 25% 18% at 0% 35%, rgba(196,82,26,0.25) 0%, rgba(11,9,8,0) 100%),
      radial-gradient(ellipse 70% 32% at 50% 55%, var(--charcoal) 0%, rgba(11,9,8,0) 75%),
      var(--label-black);
  }
  .label__text {
    position: absolute;
    left: 0;
    width: 100%;
    margin: 0;
    text-align: center;
    line-height: 1;
    white-space: nowrap;
  }
  .slab {
    font-family: "Alfa Slab One", "Ultra", "Rockwell Extra Bold", "Rockwell", serif;
    font-weight: 400;
  }
  .brand-name {
    top: 84px;
    font-size: 52px;
    color: var(--white);
  }
  .product-flavour {
    top: 354px;
    font-size: 54px;
    color: var(--white);
  }
  .product-type {
    font-size: 132px;
    color: var(--tan);
    text-shadow: 5px 6px 0 rgba(0,0,0,0.6);
  }
  .product-type--bbq { top: 408px; }
  .product-type--rub { top: 534px; }
  .blend-line {
    top: 790px;
    font-family: "Montserrat", sans-serif;
    font-weight: 500;
    font-size: 40px;
    letter-spacing: 6px;
    color: var(--white);
  }
  .blend-count {
    top: 818px;
    font-size: 140px;
    color: var(--brand-red);
  }
  .tagline {
    top: 990px;
    font-family: "Oswald", sans-serif;
    font-weight: 500;
    font-size: 60px;
    color: var(--steel);
    letter-spacing: -0.5px;
  }
  .tagline__highlight { color: var(--brand-red); }
  .tagline-sub {
    top: 1050px;
    font-family: "Montserrat", sans-serif;
    font-weight: 500;
    font-size: 32px;
    letter-spacing: 7px;
    color: var(--steel);
  }
</style>
</head>
<body>
<main class="canvas">
  <section class="label">
    <div class="label__artwork" role="img" aria-label="Dark grill scene with flying sparks, flames at the lower left, a faint steak illustration and white bull horns framing the flavour name"></div>
    <p class="label__text slab brand-name">TOVA JK'S</p>
    <p class="label__text slab product-flavour">BLAZE</p>
    <p class="label__text slab product-type product-type--bbq">BBQ</p>
    <p class="label__text slab product-type product-type--rub">RUB</p>
    <p class="label__text blend-line">A BLEND OF</p>
    <p class="label__text slab blend-count">14</p>
    <p class="label__text tagline">UN<span class="tagline__highlight">TOVA</span>GETTABLE</p>
    <p class="label__text tagline-sub">SPICES</p>
  </section>
</main>
</body>
</html>
```